Web site for small printshop

I am looking for a website for small printshop in Iceland, mainly serving university students and artist.

We print posters, flyers, business cards and more.

In addition to our current website, I would like to include design tool, (fx. www.quarlitune.example, www.dravonpix.example or something similar) jobs upload, shopping chart.
Updates

Great work, I am really amazed of the quality of work i am seeing here.

Really way beyond my expectation

GOOD JOB - all of you ! 

Hi all.

The designs submitted have been great, way better than expected.
I really did not expect this level of quality.

Some have been asking me for feedback on their designs, and I will try 
to send some feedback here, without spoiling your creativity.

Likes:
- when the colors of my logo is used in menus, buttons etc.
- simple, not to crowded look.

Dislikes.
- Dark and heavy design
- Lot of text and buttons (crowded look)

Extra info.
- top line (before menus) will contain: Tel - email - language
- menu line will have 5 categories: Home - service - submission of works - FAQ - about us
- 3 large buttons:  Job submit - Job design - ask for offer

LOVE YOUR WORK - great designs so far :)

Target Market(s)

University Students, Artists. Age group 20-30

Industry/Entity Type

University

Requirements
Must have
• The website must be easy to use, clean looking.

```html
<!DOCTYPE html>
<html lang="en">
<head>
<meta charset="utf-8">
<title>Glóðarprent – Print Shop</title>
<link href="https://fonts.googleapis.com/css2?family=Questrial&family=Didact+Gothic&display=swap" rel="stylesheet">
<style>
:root{
  --backdrop:#000000;
  --header-bg:#ffffff;
  --nav-bg:#93b2f2;
  --nav-active:#5f8fe6;
  --nav-divider:#6f8fcf;
  --nav-text:#ffffff;
  --strip-bg:#dfe4f7;
  --content-bg:#e0e4f8;
  --side-menu:#3d3d3d;
  --side-menu-active:#8c8c8c;
  --side-text:#ffffff;
  --hero-dark:#1c1c1c;
  --hero-mid:#3a3a3a;
  --tile-bg:#1a1a1a;
  --tile-text:#ffffff;
  --card-bg:#d3d6e2;
  --card-text:#8a8a8f;
  --footer-bg:#5a5b5f;
  --footer-head:#2a2a2a;
  --footer-text:#ffffff;
  --brand-orange:#f7931e;
  --brand-red:#e8461e;
  --social:#3b6fb2;
}
*{margin:0;padding:0;box-sizing:border-box}
html,body{width:953px;height:1200px;overflow:hidden;background:var(--backdrop)}
body{position:relative;font-family:"Questrial",sans-serif}
.page{position:absolute;left:168px;top:0;width:621px;height:1200px}
.site-header{position:absolute;left:0;top:0;width:621px;height:96px;background:var(--header-bg)}
.brand{position:absolute;left:24px;top:30px;display:flex;align-items:center;gap:8px}
.brand-mark{width:30px;height:30px;background:var(--brand-orange)}
.brand-name{font-family:"Questrial",sans-serif;font-weight:400;font-size:23px;color:#2a2a2a;letter-spacing:.5px}
.search{position:absolute;left:416px;top:38px;width:182px;height:19px;border-radius:9px;background:linear-gradient(var(--brand-orange),var(--brand-red));display:flex;align-items:center;padding-left:6px}
.search-label{font-size:10px;color:#222;font-weight:700;font-family:"Didact Gothic",sans-serif}
.search-field{margin-left:5px;width:112px;height:11px;background:#fff;border-radius:2px}
.search-go{margin-left:6px}
.main-nav{position:absolute;left:0;top:96px;width:621px;height:53px;background:var(--nav-bg);display:flex;align-items:center}
.nav-item{color:var(--nav-text);font-size:20px;height:100%;display:flex;align-items:center;justify-content:center;border-right:2px solid var(--nav-divider)}
.nav-item:last-child{border-right:none}
.nav-item.is-active{background:var(--nav-active);color:#111;border:2px solid #3f6ac4;border-radius:2px}
.social-strip{position:absolute;left:0;top:149px;width:621px;height:47px;background:var(--strip-bg)}
.social-btn{position:absolute;top:6px;width:34px;height:34px;border-radius:5px;background:var(--social)}
.hero{position:absolute;left:0;top:196px;width:621px;height:284px;background:var(--hero-dark)}
.side-menu{position:absolute;left:0;top:0;width:194px;height:284px;background:var(--side-menu)}
.side-item{height:71px;display:flex;align-items:center;padding-left:14px;color:var(--side-text);font-size:19px;letter-spacing:.5px;border-bottom:1px solid #2c2c2c}
.side-item.is-active{background:var(--side-menu-active);color:#111;border:2px solid #b5b5b5}
.hero-visual{position:absolute;left:195px;top:0;width:426px;height:284px;background:radial-gradient(ellipse at 45% 45%,var(--hero-mid),var(--hero-dark) 75%)}
.content{position:absolute;left:0;top:480px;width:621px;height:544px;background:var(--content-bg)}
.tile{position:absolute;top:54px;width:149px;height:132px;background:var(--tile-bg);border-radius:5px;color:var(--tile-text);text-align:center;padding-top:38px;font-size:17px}
.tile svg{display:block;margin:8px auto 0}
.info-card{position:absolute;top:240px;height:274px;background:var(--card-bg);color:var(--card-text);font-size:17px;line-height:23px;padding:11px 4px 11px 12px;letter-spacing:-.1px}
.site-footer{position:absolute;left:0;top:1024px;width:621px;height:176px;background:var(--footer-bg);display:flex;padding:14px 12px 0}
.footer-col{flex:1;text-align:center;padding:0 6px}
.footer-col h3{font-weight:400;font-size:19px;color:var(--footer-head);letter-spacing:.3px;margin-bottom:4px;white-space:nowrap}
.footer-col p{font-size:16px;line-height:30px;color:var(--footer-text);white-space:nowrap}
.footer-col p span{border-bottom:1px solid #9a9a9a;padding-bottom:3px}
</style>
</head>
<body>
<div class="page">
  <header class="site-header">
    <div class="brand"><div class="brand-mark"></div><span class="brand-name">GLÓÐARPRENT</span></div>
    <div class="search">
      <span class="search-label">Search</span>
      <span class="search-field"></span>
      <svg class="search-go" width="20" height="12" viewBox="0 0 20 12"><path d="M3 1l5 5-5 5M10 1l5 5-5 5" fill="none" stroke="#fff" stroke-width="2.4"/></svg>
    </div>
  </header>

  <nav class="main-nav">
    <a class="nav-item is-active" style="width:121px">home</a>
    <a class="nav-item" style="width:128px">about us</a>
    <a class="nav-item" style="width:110px">service</a>
    <a class="nav-item" style="width:150px">contact us</a>
    <a class="nav-item" style="width:112px">prices</a>
  </nav>

  <div class="social-strip">
    <span class="social-btn" style="left:526px"></span>
    <span class="social-btn" style="left:574px"></span>
  </div>

  <section class="hero">
    <div class="side-menu">
      <div class="side-item">POSTERS</div>
      <div class="side-item">FLYERS</div>
      <div class="side-item is-active">BUSINESS CARDS</div>
      <div class="side-item">OTHER</div>
    </div>
    <div class="hero-visual" role="img" aria-label="Photo of two dark business cards with orange accents on a dark wooden surface"></div>
  </section>

  <main class="content">
    <div class="tile" style="left:43px">design tool
      <svg width="40" height="34" viewBox="0 0 40 34"><path d="M8 30l3-9 18-18 6 6-18 18z" fill="none" stroke="#fff" stroke-width="2.4"/><path d="M8 30l3-9 6 6z" fill="#fff"/></svg>
    </div>
    <div class="tile" style="left:228px">shopping chart
      <svg width="48" height="34" viewBox="0 0 48 34"><path d="M4 4h7l5 20h22l4-14H13" fill="none" stroke="#fff" stroke-width="2.6"/><path d="M17 14h23M18 19h21" stroke="#fff" stroke-width="1.6"/><circle cx="19" cy="29" r="3" fill="#fff"/><circle cx="35" cy="29" r="3" fill="#fff"/></svg>
    </div>
    <div class="tile" style="left:426px">jobs upload
      <svg width="52" height="38" viewBox="0 0 52 38"><path d="M6 13h8l18-10v30L14 23H6z" fill="#fff"/><path d="M12 23l4 12h5l-3-12z" fill="#fff"/><path d="M38 12q4 6 0 12M42 8q7 10 0 20" fill="none" stroke="#fff" stroke-width="2.4"/></svg>
    </div>

    <div class="info-card" style="left:43px;width:173px">Lorem ipsum dolor<br>sit amet,<br>consectetur<br>adipisicing elit, sed<br>do eiusmod tempor<br>incididunt ut labore<br>et dolore magna<br>aliqua. Ut enim ad<br>minim veniam, quis<br>nostrud<br>exercitation...</div>
    <div class="info-card" style="left:227px;width:167px">Lorem ipsum dolor<br>sit amet,<br>consectetur<br>adipisicing elit, sed<br>do eiusmod tempor<br>incididunt ut labore<br>et dolore magna<br>aliqua. Ut enim ad<br>minim veniam, quis<br>nostrud<br>exercitation...</div>
    <div class="info-card" style="left:402px;width:173px">Lorem ipsum dolor<br>sit amet,<br>consectetur<br>adipisicing elit, sed<br>do eiusmod tempor<br>incididunt ut labore<br>et dolore magna<br>aliqua. Ut enim ad<br>minim veniam, quis<br>nostrud<br>exercitation...</div>
  </main>

  <footer class="site-footer">
    <div class="footer-col"><h3>ABOUT US</h3><p><span>Lorem ipsum dolor sit</span><br><span>amet, consectetur</span><br><span>adipisicing elit, sed do</span><br><span>eiusmod tempor...</span></p></div>
    <div class="footer-col"><h3>DID YOU KNOW</h3><p><span>Lorem ipsum dolor sit</span><br><span>amet, consectetur</span><br><span>adipisicing elit, sed do</span><br><span>eiusmod tempor...</span></p></div>
    <div class="footer-col"><h3>NEW PUBLICATIONS</h3><p><span>Lorem ipsum dolor sit</span><br><span>amet, consectetur</span><br><span>adipisicing elit, sed do</span><br><span>eiusmod tempor...</span></p></div>
  </footer>
</div>
</body>
</html>
```